Modern corporate energy/fuel business need business card design

Business card required for company founder. Korvan Specialised Energy is a Australian based modern energy/fuel provider. We offer specialised solutions to businesses using fossil fuels through renewable energy solutions.

I would like one side with specific information (name, address etc)

The other side to be bold, professional company name & logo. Striking.

Target Market(s)

B2B. Transport, mining, councils, environmentalist,

Industry/Entity Type

Petroleum

Contact Information for Business Card

Name; Peter Morrow
Position; Director
Email; pmorrow@korvanse.com.au
Address; PO Box 347, Ardenvale, QLD, 4870
Website; www.korvanse.com.au

Colors

Designer to choose colors to be used in the design.

Requirements
Must have
• Clean, easy to read, professional & strong theme
Should not have
• too many colours, busy layout,

```html
<!DOCTYPE html>
<html lang="en">
<head>
<meta charset="utf-8">
<title>Korvan Specialised Energy – Business Card</title>
<link rel="stylesheet" href="https://fonts.googleapis.com/css2?family=Montserrat:wght@300;400;700&display=swap">
<style>
  :root {
    --navy: #23557a;
    --orange: #f28323;
    --white: #ffffff;
    --ink: #1f2a33;
    --backdrop: #cfcecb;
  }
  * { margin: 0; padding: 0; box-sizing: border-box; }
  html, body { width: 1200px; height: 801px; overflow: hidden; }
  body {
    background: var(--backdrop);
    font-family: "Montserrat", sans-serif;
    position: relative;
  }
  .card {
    position: absolute;
    top: 235px;
    width: 540px;
    height: 330px;
    overflow: hidden;
    box-shadow: 0 10px 24px rgba(0,0,0,0.22);
  }
  .card--front { left: 40px; background: var(--white); }
  .card--back { left: 620px; background: var(--navy); }

  .front-sweep { position: absolute; inset: 0; }

  .company-name {
    position: absolute;
    font-weight: 700;
    text-transform: uppercase;
    white-space: nowrap;
  }
  .card--front .company-name {
    left: 30px; top: 44px;
    color: var(--navy);
    font-size: 15px;
    letter-spacing: 1.5px;
  }
  .card--back .company-name {
    left: 0; right: 0; top: 148px;
    text-align: center;
    color: var(--white);
    font-size: 26px;
    letter-spacing: 2px;
  }

  .person { position: absolute; left: 30px; top: 112px; }
  .person__name { color: var(--navy); font-weight: 700; font-size: 20px; }
  .person__role { color: var(--orange); font-weight: 300; font-size: 14px; margin-top: 2px; }

  .rule {
    position: absolute; left: 30px; top: 172px;
    width: 300px; height: 1px; background: var(--navy);
  }
  .contact {
    position: absolute; left: 30px; top: 186px;
    list-style: none; color: var(--ink);
    font-size: 12.5px; font-weight: 400;
  }
  .contact li { display: flex; align-items: center; gap: 8px; height: 24px; }
  .contact__icon { width: 12px; height: 12px; flex: none; }
</style>
</head>
<body>

<section class="card card--front" aria-label="Business card front">
  <svg class="front-sweep" viewBox="0 0 540 330" width="540" height="330" aria-hidden="true">
    <path d="M505 0 H540 V330 H44 C330 262 500 150 505 0 Z" fill="var(--navy)"/>
    <path d="M489 0 C484 150 318 262 8 330" fill="none" stroke="var(--orange)" stroke-width="6"/>
  </svg>

  <p class="company-name">Korvan Specialised Energy</p>

  <div class="person">
    <p class="person__name">Peter Morrow</p>
    <p class="person__role">Director</p>
  </div>

  <div class="rule"></div>

  <ul class="contact">
    <li>PO Box 347, Ardenvale, QLD, 4870</li>
    <li>
      <svg class="contact__icon" viewBox="0 0 12 12" aria-hidden="true">
        <rect x="0.5" y="2" width="11" height="8" fill="var(--orange)"/>
        <path d="M1 2.5 L6 6.5 L11 2.5" fill="none" stroke="var(--white)" stroke-width="1.2"/>
      </svg>
      pmorrow@korvanse.com.au
    </li>
    <li>
      <svg class="contact__icon" viewBox="0 0 12 12" aria-hidden="true">
        <circle cx="6" cy="6" r="5.5" fill="var(--orange)"/>
        <path d="M0.8 6 H11.2 M6 0.8 C3.5 3.5 3.5 8.5 6 11.2 M6 0.8 C8.5 3.5 8.5 8.5 6 11.2" fill="none" stroke="var(--white)" stroke-width="0.8"/>
      </svg>
      www.korvanse.com.au
    </li>
  </ul>
</section>

<section class="card card--back" aria-label="Business card back">
  <p class="company-name">Korvan Specialised Energy</p>
</section>

</body>
</html>
```